we need a business card design for a professional painting business. This company has been up and going for about ten years. However it needs an new logo. we want this business card to be modern eye catching and easy to read. I currently have been looking for VP logos but can not find one that suits our needs. This Design should be Our start to a new beginning.
Industry/Entity Type
Painting
Contact Information for Business Card
Varesko Painting Inc.
Licensed & Insured
Tomas Varesko
Phone(631)384-4562
Fax (555) 846-3021
E-mail vareskopaintinginc@mailorbit.test
Requirements
Must have
- a new logo with  VP and i would like it to be in black and white.
i would also like the front to be a solid black with the logo only and then the back to have the information.

```html
<!DOCTYPE html>
<html lang="en">
<head>
<meta charset="UTF-8">
<title>Varesko Painting Inc. — Business Card</title>
<link rel="stylesheet" href="https://fonts.googleapis.com/css2?family=Open+Sans:wght@400;600;700&display=swap">
<style>
  :root {
    --backdrop: #dcdcdc;
    --card-black: #1b1b1b;
    --card-white: #f4f4f4;
    --ink: #1e1e1e;
    --paper-text: #ffffff;
    --muted: #9a9a9a;
    --roller: #7d7d7d;
  }
  * { margin: 0; padding: 0; box-sizing: border-box; }
  html, body {
    width: 1200px; height: 900px; overflow: hidden;
    background: var(--backdrop);
    font-family: "Open Sans", Arial, sans-serif;
  }
  .canvas {
    width: 1200px; height: 900px;
    display: flex; align-items: center; justify-content: center; gap: 60px;
  }
  .card {
    width: 520px; height: 297px; position: relative; overflow: hidden;
    box-shadow: 0 6px 18px rgba(0,0,0,0.18);
  }
  /* Front */
  .card-front {
    background: var(--card-black);
    display: flex; align-items: center; justify-content: center; gap: 14px;
  }
  .brand-square {
    width: 34px; height: 34px; border: 3px solid var(--paper-text); border-radius: 6px;
  }
  .brand-name {
    color: var(--paper-text); font-weight: 700; font-size: 26px; letter-spacing: 0.3px;
  }
  /* Back */
  .card-back { background: var(--card-white); }
  .paint-band {
    position: absolute; left: 62px; top: 52px; width: 380px; height: 62px;
    background: var(--ink);
    padding: 10px 0 0 22px; color: var(--paper-text);
  }
  .band-title { font-weight: 700; font-size: 19px; line-height: 1.15; }
  .band-sub { font-weight: 400; font-size: 11.5px; margin-top: 2px; }
  .roller {
    position: absolute; left: 440px; top: 38px; width: 32px; height: 82px;
    background: var(--roller); border-radius: 4px;
  }
  .contact-list {
    position: absolute; left: 84px; top: 134px; list-style: none;
    color: var(--ink); font-size: 15px;
  }
  .contact-item { display: flex; align-items: center; gap: 10px; height: 23px; }
  .contact-icon { width: 14px; height: 14px; flex: none; }
</style>
</head>
<body>
<main class="canvas">
  <section class="card card-front" aria-label="Card front">
    <span class="brand-square"></span>
    <span class="brand-name">Varesko Painting Inc.</span>
  </section>

  <section class="card card-back" aria-label="Card back">
    <div class="paint-band">
      <p class="band-title">Varesko Painting Inc.</p>
      <p class="band-sub">Licensed &amp; Insured Tomas Varesko</p>
    </div>
    <div class="roller" role="img" aria-label="Paint roller at the end of the painted stripe"></div>
    <ul class="contact-list">
      <li class="contact-item">
        <svg class="contact-icon" viewBox="0 0 14 14" aria-hidden="true"><rect width="14" height="14" rx="3" fill="#555"/><path d="M4 3.5c.6-.4 1.2 0 1.5.7l.4.9c.2.4 0 .8-.3 1l-.4.3c.4.9 1.1 1.6 2 2l.3-.4c.2-.3.6-.5 1-.3l.9.4c.7.3 1.1.9.7 1.5-.5.8-1.3 1-2 .8C6 10 4 8 3.3 5.6c-.2-.8 0-1.6.7-2.1z" fill="#fff"/></svg>
        <span>(555)217-9083</span>
      </li>
      <li class="contact-item">
        <svg class="contact-icon" viewBox="0 0 14 14" aria-hidden="true"><rect width="14" height="14" rx="3" fill="#555"/><rect x="4" y="2.5" width="6" height="3" fill="#fff"/><rect x="2.5" y="5.5" width="9" height="4" rx="1" fill="#fff"/><rect x="4" y="8.5" width="6" height="3" fill="#ccc"/></svg>
        <span>(555) 846-3021</span>
      </li>
      <li class="contact-item">
        <svg class="contact-icon" viewBox="0 0 14 14" aria-hidden="true"><rect width="14" height="14" rx="3" fill="#555"/><rect x="2.5" y="4" width="9" height="6" fill="#fff"/><path d="M2.5 4l4.5 3.5L11.5 4" fill="none" stroke="#555" stroke-width="1"/></svg>
        <span>vareskopaintinginc@mailorbit.test</span>
      </li>
    </ul>
  </section>
</main>
</body>
</html>
```